High End Notary Service Business Card Design

Want a professional and elegant/luxurious business card that is clean and simple in the design. A notary is a trusted professional that helps people sign very important documents. The card should be in alignment with this service provided.

Most of the time, service will be for the purchase of a home or refinance of a mortgage

There is NO LOGO. This is aesthetic. A look and feel. Conveying professionalism and concierge level of service.

Target Market(s)

Other business professionals, Lawyers, Escrow Officers, Loan Officers

Industry/Entity Type

Legal

Contact Information for Business Card

This will be a one-sided business card

Colors
35a7d7
3176b5
85cae6
d3a5cc
b868aa
ffffff
0356a4

Requirements
Must have
• Lorena T. Mirabel-Hodgkins
Notary Public

642-871-3094
MirabelSigningDesk@Wexmail.com
Nice to have
• Headshot photo below. Convey the aspect of signing documents. No black cards. Preference is shades of blue: light blue, navy, aqua, gold, white, or lavendar, etc.
Should not have
• No scales or legal scales.

```html
<!DOCTYPE html>
<html lang="en">
<head>
<meta charset="utf-8">
<title>Lorena T. Mirabel-Hodgkins – Notary Public Business Card</title>
<link rel="stylesheet" href="https://fonts.googleapis.com/css2?family=Jost:wght@400&display=swap">
<style>
  :root {
    --page-bg: #f3f3f3;
    --card-navy: #1c2944;
    --card-navy-deep: #18233c;
    --gold: #cdae74;
  }
  html, body {
    margin: 0;
    width: 1200px;
    height: 1200px;
    overflow: hidden;
    background: var(--page-bg);
  }
  .business-card {
    position: absolute;
    left: 222px;
    top: 384px;
    width: 755px;
    height: 431px;
    background: var(--card-navy);
    overflow: hidden;
    font-family: "Jost", "Helvetica Neue", Arial, sans-serif;
    color: var(--gold);
  }
  .watermark-ring {
    position: absolute;
    left: 370px;
    top: 48px;
    width: 360px;
    height: 360px;
  }
  .emblem {
    position: absolute;
    left: 66px;
    top: 40px;
    width: 104px;
    height: 106px;
  }
  .identity {
    position: absolute;
    right: 87px;
    top: 56px;
    text-align: right;
    padding-right: 18px;
    border-right: 5px solid var(--gold);
  }
  .identity__name {
    margin: 0;
    font-size: 31px;
    font-weight: 400;
    letter-spacing: 0.6px;
    line-height: 40px;
    white-space: nowrap;
  }
  .identity__title {
    margin: 0;
    font-size: 22px;
    font-weight: 400;
    letter-spacing: 0.3px;
    line-height: 28px;
  }
  .contact-list {
    position: absolute;
    left: 66px;
    top: 320px;
    margin: 0;
    padding: 0;
    list-style: none;
  }
  .contact-list__item {
    display: flex;
    align-items: center;
    height: 38px;
    font-size: 22.5px;
    letter-spacing: 0.3px;
  }
  .contact-list__icon {
    width: 30px;
    height: 30px;
    margin-right: 13px;
    flex: none;
  }
</style>
</head>
<body>
  <main class="business-card">
    <svg class="watermark-ring" viewBox="0 0 360 360" aria-hidden="true">
      <circle cx="180" cy="180" r="168" fill="none" stroke="var(--card-navy-deep)" stroke-width="14"/>
    </svg>

    <svg class="emblem" viewBox="0 0 104 106" role="img" aria-label="Quill feather emblem inside a gold ring">
      <circle cx="52" cy="56" r="49" fill="none" stroke="var(--gold)" stroke-width="3"/>
    </svg>

    <header class="identity">
      <h1 class="identity__name">Lorena T. Mirabel-Hodgkins</h1>
      <p class="identity__title">Notary Public</p>
    </header>

    <ul class="contact-list">
      <li class="contact-list__item">
        <svg class="contact-list__icon" viewBox="0 0 30 30" aria-hidden="true">
          <circle cx="15" cy="15" r="13" fill="none" stroke="var(--gold)" stroke-width="2"/>
          <path d="M10.5 8.5c.6-.6 1.5-.6 2 0l1.4 1.8c.4.5.3 1.2-.1 1.6l-.9.8c.7 1.6 1.9 2.9 3.5 3.7l.8-.9c.4-.5 1.1-.5 1.6-.1l1.8 1.4c.6.5.6 1.4 0 2l-.9.9c-.8.8-2 1-3 .6-3.3-1.4-5.9-4-7.3-7.3-.4-1-.2-2.2.6-3z" fill="none" stroke="var(--gold)" stroke-width="1.6" stroke-linejoin="round"/>
        </svg>
        <span>642 - 871 - 3094</span>
      </li>
      <li class="contact-list__item">
        <svg class="contact-list__icon" viewBox="0 0 30 30" aria-hidden="true">
          <circle cx="15" cy="15" r="13" fill="none" stroke="var(--gold)" stroke-width="2"/>
          <rect x="8.5" y="10" width="13" height="10" rx="1.2" fill="none" stroke="var(--gold)" stroke-width="1.6"/>
          <path d="M9 11l6 4.5 6-4.5" fill="none" stroke="var(--gold)" stroke-width="1.6" stroke-linejoin="round"/>
        </svg>
        <span>MirabelSigningDesk@Wexmail.com</span>
      </li>
    </ul>
  </main>
</body>
</html>
```